Buchcover für mittelständige Unternehmen die positive Bewertungen erhalten möchten
Zielgruppe
Was macht die Firma: Unternehmensberatung für den Personlabereich
Zielgruppe: Unternehmer aus dem mittelständigen Bereich die positive Bewertungen auf Portalen wie werkrat, deskmirror und Plomix erhalten möchten.
Aufgabenstellung
Ansprechend, Professionell, Positive Aussendarstellung des Unternehmens

```html
<!DOCTYPE html>
<html lang="de">
<head>
<meta charset="utf-8">
<title>Positive Bewertungen? – Buchcover</title>
<link rel="stylesheet" href="https://fonts.googleapis.com/css2?family=Poppins:ital,wght@0,300;0,700;1,300&display=swap">
<style>
  :root {
    --teal: #003c57;
    --paper: #ffffff;
    --stage: #dfe5e9;
    --photo-warm: #e8973a;
    --photo-sand: #dcc7ad;
    --photo-suit: #5f5a56;
    --photo-mid: #8a847e;
    --photo-light: #d9d4ce;
  }
  * { margin: 0; padding: 0; box-sizing: border-box; }
  html, body {
    width: 1200px;
    height: 848px;
    overflow: hidden;
    background: var(--stage);
    font-family: "Poppins", sans-serif;
  }
  .book-cover {
    position: absolute;
    left: 330px;
    top: 44px;
    width: 540px;
    height: 760px;
    background: var(--paper);
    overflow: hidden;
    box-shadow: 0 10px 30px rgba(0, 40, 60, 0.18);
  }
  .cover-art {
    position: absolute;
    inset: 0;
    width: 540px;
    height: 760px;
  }
  .cover-title {
    position: absolute;
    left: 40px;
    top: 62px;
    color: var(--teal);
    font-weight: 700;
    font-size: 48px;
    line-height: 1.08;
    letter-spacing: -0.5px;
  }
  .cover-subtitle {
    position: absolute;
    left: 42px;
    top: 186px;
    color: var(--teal);
    font-weight: 300;
    font-style: italic;
    font-size: 21px;
  }
  .cover-author {
    position: absolute;
    left: 0;
    right: 0;
    top: 690px;
    height: 70px;
    line-height: 70px;
    text-align: center;
    color: var(--paper);
    font-weight: 300;
    font-size: 24px;
    letter-spacing: 0.3px;
  }
</style>
</head>
<body>
  <main class="book-cover">
    <svg class="cover-art" viewBox="0 0 540 760" xmlns="http://www.w3.org/2000/svg">
      <defs>
        <linearGradient id="photoBase" x1="0" y1="0" x2="1" y2="1">
          <stop offset="0" stop-color="var(--photo-warm)"/>
          <stop offset="0.28" stop-color="var(--photo-sand)"/>
          <stop offset="0.5" stop-color="var(--photo-suit)"/>
          <stop offset="0.75" stop-color="var(--photo-mid)"/>
          <stop offset="1" stop-color="var(--photo-light)"/>
        </linearGradient>
        <radialGradient id="photoGlow" cx="0.78" cy="0.35" r="0.45">
          <stop offset="0" stop-color="#ffffff" stop-opacity="0.55"/>
          <stop offset="1" stop-color="#ffffff" stop-opacity="0"/>
        </radialGradient>
        <linearGradient id="wedgeShade" x1="0" y1="0" x2="1" y2="0">
          <stop offset="0" stop-color="#000000" stop-opacity="0.10"/>
          <stop offset="1" stop-color="#000000" stop-opacity="0"/>
        </linearGradient>
      </defs>
      <g class="cover-photo" role="img" aria-label="Foto: Geschäftsmann im Anzug tippt auf fünf leuchtende Bewertungssterne">
        <polygon points="0,430 483,343 540,441 540,690 0,690" fill="url(#photoBase)"/>
        <polygon points="0,430 483,343 540,441 540,690 0,690" fill="url(#photoGlow)"/>
      </g>
      <polygon class="cover-light-band" points="0,430 483,343 513,394 0,532" fill="#ffffff" opacity="0.2"/>
      <line class="cover-band-edge" x1="0" y1="532" x2="513" y2="394" stroke="#ffffff" stroke-opacity="0.45" stroke-width="1.5"/>
      <polygon class="cover-wedge-shadow" points="300,28 314,28 554,441 540,441" fill="url(#wedgeShade)"/>
      <rect class="cover-top-band" x="0" y="0" width="540" height="28" fill="var(--teal)"/>
      <rect class="cover-bottom-band" x="0" y="690" width="540" height="70" fill="var(--teal)"/>
    </svg>
    <h1 class="cover-title">Positive<br>Bewertungen?</h1>
    <p class="cover-subtitle">Wir verraten Ihnen das Geheimnis</p>
    <p class="cover-author">Max Mustermann</p>
  </main>
</body>
</html>
```